Coffee roasting needs homepage with web shop

small roasting (no cafe!) needs a simple website with a web shop. We sell coffee to dealers and end customers. The shop should be for end consumers as well as for B2B customers. A login should be available. The design should be modern and at the same time classic with subtle (dark) colors. We need the tabs "Coffee, Shop, Contact, Coffee, Coffee, Login, About Us, Imprint, Privacy" Logo nr 1 should be used from attached file

Target Market(s)

B2B

Number of Pages Required

5+ page

Font styles to use
Sans Serif

Colors

Designer to choose only greyscale colors for use in the design.

Requirements
Must have
• Webshop

```html
<!DOCTYPE html>
<html lang="en">
<head>
<meta charset="utf-8">
<title>Kornhaus – Premier Specialty Coffee Roaster</title>
<link href="https://fonts.googleapis.com/css2?family=Roboto:wght@400;500;700;900&family=Quicksand:wght@400;500;600&family=Lato:wght@400;700&display=swap" rel="stylesheet">
<style>
:root{
  --brown-dark:#3a1a0c;
  --brown-bar:#6a3414;
  --brown-nav:#6b3a1c;
  --tan:#b88c5e;
  --tan-light:#c7a27a;
  --grey-nav:#dcdcdc;
  --grey-btn:#e0e0e0;
  --ink:#2b2b2b;
  --muted:#8a8a8a;
  --footer-bg:#f7f5f2;
  --copy-bg:#e6e6e6;
  --white:#fff;
}
*{box-sizing:border-box;margin:0;padding:0}
html,body{width:1200px;height:3160px;overflow:hidden;background:var(--white)}
body{position:relative;font-family:'Quicksand',sans-serif;color:var(--ink)}
.abs{position:absolute}
.topbar{left:0;top:0;width:1200px;height:47px;background:var(--brown-bar);color:var(--white);font:500 15px 'Quicksand',sans-serif;letter-spacing:1px}
.topbar span{position:absolute;top:12px;display:flex;align-items:center;gap:8px}
.navbar{left:0;top:47px;width:1200px;height:66px;background:var(--grey-nav)}
.navbar a{position:absolute;top:0;height:66px;font:700 15px 'Roboto',sans-serif;line-height:66px;letter-spacing:1px;color:var(--brown-nav);text-decoration:none}
.navbar a.active{background:var(--white);padding:0 14px;color:var(--brown-dark)}
.brand-badge{left:97px;top:18px;width:166px;height:166px;border-radius:50%;background:var(--white);border:3px solid var(--brown-dark);box-shadow:0 0 0 5px var(--white);display:flex;align-items:center;justify-content:center;font:600 24px 'Quicksand',sans-serif;color:var(--brown-dark);z-index:3}
.hero{left:0;top:113px;width:1200px;height:499px;background:radial-gradient(ellipse at 60% 40%,#7a4a2a,#3b200f 70%,#1e0f07)}
.hero h1{position:absolute;left:446px;top:300px;font:900 64px 'Roboto',sans-serif;line-height:1;color:var(--white);letter-spacing:2px}
.hero h2{position:absolute;left:446px;top:370px;font:700 43px 'Roboto',sans-serif;color:var(--white);letter-spacing:2px}
.btn-light{position:absolute;background:var(--grey-btn);color:var(--brown-nav);font:700 16px 'Roboto',sans-serif;letter-spacing:1px;display:flex;align-items:center;justify-content:center}
.story-left{left:0;top:612px;width:595px;height:455px;background:var(--brown-dark);color:var(--white)}
.story-left h2{position:absolute;left:78px;top:50px;font:400 50px 'Quicksand',sans-serif;letter-spacing:3px}
.story-left p{position:absolute;left:78px;top:122px;width:460px;font:500 14px/21.5px 'Quicksand',sans-serif}
.story-right{left:595px;top:612px;width:605px;height:455px;background:radial-gradient(ellipse at 50% 50%,#6b5a50,#b8b2ad 55%,#eceae8)}
.promo{top:1081px;width:321px;height:312px;color:var(--white);padding:112px 0 0 12px}
.promo h3{font:700 27px 'Roboto',sans-serif;letter-spacing:2px;color:var(--tan-light)}
.promo h4{font:500 18px 'Quicksand',sans-serif;letter-spacing:2px;margin-top:10px}
.promo .shop{margin-top:18px;width:171px;height:49px;border:2px solid var(--white);display:flex;align-items:center;justify-content:center;font:700 14px 'Roboto',sans-serif;letter-spacing:1px}
.promo .shop.filled{background:var(--tan);border-color:var(--tan)}
.sec-kicker{left:88px;top:1426px;font:400 27px 'Quicksand',sans-serif;color:var(--brown-nav);letter-spacing:1px}
.sec-title{left:86px;top:1464px;font:400 31px 'Quicksand',sans-serif;letter-spacing:2px}
.dots{left:90px;top:1510px;display:flex;gap:5px}
.dots i{width:8px;height:8px;border-radius:50%;background:var(--ink)}
.arrow{top:1473px;width:34px;height:34px;border:1px solid var(--tan);display:flex;align-items:center;justify-content:center}
.product{top:1548px;width:321px}
.product .photo{height:272px;background:linear-gradient(180deg,#9aa6ad 0%,#c8b39a 60%,#8a5f3a 100%);position:relative}
.product .sale{position:absolute;left:8px;top:22px;background:var(--white);padding:3px 8px;font:500 16px 'Roboto',sans-serif}
.product .cartbar{position:absolute;left:0;bottom:0;width:100%;height:50px;display:flex}
.product .cartbar .add{flex:1;background:var(--tan);color:var(--white);font:700 14px 'Lato',sans-serif;letter-spacing:1px;display:flex;align-items:center;justify-content:center}
.product .cartbar .fav{width:52px;background:var(--tan-light);display:flex;align-items:center;justify-content:center}
.product .row1{display:flex;justify-content:space-between;margin-top:20px;padding-bottom:8px;border-bottom:1px solid #ddd}
.product .name{font:700 17px 'Lato',sans-serif;letter-spacing:2px}
.product .price{font:400 17px 'Lato',sans-serif;color:var(--tan)}
.product .price s{color:var(--muted);font-size:14px;margin-right:6px}
.product .row2{display:flex;justify-content:space-between;margin-top:12px;font:400 13px 'Lato',sans-serif;color:var(--muted)}
.stars{color:var(--tan);letter-spacing:1px}
.deliver-img{left:93px;top:1990px;width:677px;height:433px;background:linear-gradient(90deg,#5a3a24,#9a8a7c 40%,#c9c3bd 60%,#6b4a32)}
.deliver-box{left:624px;top:2038px;width:484px;height:328px;background:var(--white);border:1px solid #ddd;padding:34px 44px}
.deliver-box h2{font:400 31px 'Quicksand',sans-serif;letter-spacing:2px}
.deliver-box p{margin-top:26px;font:500 14px/27px 'Quicksand',sans-serif}
.deliver-badge{left:540px;top:1944px;width:94px;height:94px;border-radius:50%;background:var(--white);border:2px solid var(--brown-dark);box-shadow:0 0 0 4px var(--white);display:flex;align-items:center;justify-content:center;font:600 14px 'Quicksand',sans-serif;color:var(--brown-dark)}
.newsletter{left:0;top:2440px;width:1200px;height:320px;background:linear-gradient(180deg,#8a8a8a 0%,#c9c9c9 20%,#e2e2e2 50%,#c9c9c9 80%,#8a8a8a 100%)}
.newsletter h2{position:absolute;width:100%;top:104px;text-align:center;font:400 30px 'Quicksand',sans-serif;letter-spacing:2px}
.newsletter .field{position:absolute;left:357px;top:154px;width:440px;height:56px;background:var(--white);border:1px solid #bbb;padding:0 22px;font:400 14px 'Lato',sans-serif;line-height:54px;color:var(--muted)}
.newsletter .subscribe{position:absolute;left:797px;top:154px;width:149px;height:56px;background:var(--tan);color:var(--white);font:700 15px 'Roboto',sans-serif;display:flex;align-items:center;justify-content:center}
.footer{left:0;top:2760px;width:1200px;height:315px;background:var(--footer-bg)}
.footer .badge{position:absolute;left:148px;top:28px;width:84px;height:84px;border-radius:50%;border:2px solid var(--brown-dark);display:flex;align-items:center;justify-content:center;font:600 14px 'Quicksand',sans-serif;color:var(--brown-dark)}
.footer .contact{position:absolute;left:124px;font:400 11px/13px 'Quicksand',sans-serif;color:var(--muted);display:flex;gap:12px}
.footer .col{position:absolute;top:68px}
.footer .col h5{font:600 13px 'Quicksand',sans-serif;letter-spacing:1px;padding-bottom:8px;border-bottom:1px solid var(--brown-nav);display:inline-block;margin-bottom:8px}
.footer .col li{list-style:none;font:400 11px/25px 'Quicksand',sans-serif;color:var(--muted)}
.footer .social{display:flex;gap:14px;margin-top:12px}
.footer .social i{width:20px;height:20px;background:var(--brown-dark);display:block}
.cup{left:1000px;top:2930px;width:190px;height:130px;background:radial-gradient(circle at 30% 50%,#6b4a3a 18%,#e6e2de 26%,#f7f5f2 40%),radial-gradient(circle at 75% 50%,#8a5a3a,transparent 60%)}
.copy{left:0;top:3075px;width:1200px;height:85px;background:var(--copy-bg);text-align:center;font:400 11px 'Quicksand',sans-serif;line-height:85px;color:var(--muted)}
</style>
</head>
<body>
<header>
  <div class="abs topbar">
    <span style="left:659px"><svg width="18" height="18" viewBox="0 0 18 18"><circle cx="7.5" cy="7.5" r="6" fill="none" stroke="#fff" stroke-width="2"/><path d="M12 12l5 5" stroke="#fff" stroke-width="2"/></svg>SEARCH</span>
    <span style="left:796px"><svg width="22" height="18" viewBox="0 0 22 18"><path d="M1 2h3l2 10h12l2-7H6" fill="none" stroke="#fff" stroke-width="1.6"/><circle cx="8" cy="15.5" r="1.5" fill="#fff"/><circle cx="17" cy="15.5" r="1.5" fill="#fff"/></svg>CART</span>
    <span style="left:907px"><svg width="22" height="22" viewBox="0 0 22 22"><circle cx="11" cy="11" r="10" fill="none" stroke="#fff" stroke-width="1.6"/><circle cx="11" cy="9" r="3.5" fill="#fff"/><path d="M5 17c2-4 10-4 12 0" fill="#fff"/></svg>&nbsp;REGISTER / LOG IN</span>
  </div>
  <nav class="abs navbar">
    <a class="active" style="left:359px">COFFEE</a>
    <a style="left:480px">ABOUT US</a>
    <a style="left:603px">SHOP</a>
    <a style="left:694px">LOGIN</a>
    <a style="left:785px">IMPRINT</a>
    <a style="left:900px">PRIVACY</a>
    <a style="left:1023px">CONTACT</a>
  </nav>
  <div class="abs brand-badge">Kornhaus</div>
</header>

<section class="abs hero" role="img" aria-label="Hand stirring freshly roasted coffee beans in a roasting drum">
  <h1>PREMIER SPECIALTY</h1>
  <h2>COFFEE ROASTER</h2>
  <div class="btn-light" style="left:918px;top:409px;width:203px;height:60px">KNOW MORE</div>
</section>

<section>
  <div class="abs story-left">
    <h2>OUR STORY</h2>
    <p>Lorem ipsum dolor sit amet, consectetur adipiscing elit, sed do eiusmod tempor incididunt ut labore et dolore magna aliqua. Ut enim ad minim veniam, quis nostrud exercitation ullamco laboris nisi ut aliquip ex ea commodo consequat. Duis aute irure dolor in reprehenderit in voluptate velit esse cillum dolore eu fugiat nulla pariatur. Excepteur sint occaecat cupidatat non proident, sunt in culpa qui officia deserunt mollit anim id est laborum.</p>
    <div class="btn-light" style="left:79px;top:342px;width:204px;height:60px">KNOW MORE</div>
  </div>
  <div class="abs story-right" role="img" aria-label="Close-up of roasted coffee beans on a white surface"></div>
</section>

<section>
  <div class="abs promo" style="left:84px;background:linear-gradient(180deg,#4a3020,#2a1a10)" role="img" aria-label="Roasted beans in a bowl">
    <h3>NEW!</h3><h4>INCREDIBLE COFFEE</h4><div class="shop">SHOP NOW</div>
  </div>
  <div class="abs promo" style="left:432px;background:linear-gradient(180deg,#6a5048,#3a2418)" role="img" aria-label="Takeaway coffee cups with beans">
    <h3>SPRING UP!</h3><h4>NEW ACCESSORIES</h4><div class="shop filled">SHOP NOW</div>
  </div>
  <div class="abs promo" style="left:781px;background:linear-gradient(180deg,#3a2a22,#5a3a24)" role="img" aria-label="Espresso pouring into a cup">
    <h3>ONLY ONE!</h3><h4>DISCOUNT COFFEE</h4><div class="shop">SHOP NOW</div>
  </div>
</section>

<section>
  <div class="abs sec-kicker">Our Product</div>
  <div class="abs sec-title">FEATURED</div>
  <div class="abs dots"><i></i><i></i><i></i><i></i><i></i><i></i></div>
  <div class="abs arrow" style="left:1020px"><svg width="10" height="12"><path d="M7 1L2 6l5 5" fill="none" stroke="#b88c5e" stroke-width="1.5"/></svg></div>
  <div class="abs arrow" style="left:1063px;background:var(--tan)"><svg width="10" height="12"><path d="M3 1l5 5-5 5" fill="none" stroke="#fff" stroke-width="1.5"/></svg></div>

  <div class="abs product" style="left:90px">
    <div class="photo" role="img" aria-label="Paper coffee bag on a wooden table"><span class="sale">SALE</span></div>
    <div class="row1"><span class="name">COFFEE BEAN</span><span class="price"><s>$100</s>$ 85</span></div>
    <div class="row2"><span>Light, Flavourful. 1 kg</span><span class="stars">★★★★☆</span></div>
  </div>
  <div class="abs product" style="left:437px">
    <div class="photo" role="img" aria-label="Three paper coffee bags on a shelf">
      <div class="cartbar"><div class="add">ADD TO CART</div><div class="fav"><svg width="16" height="14" viewBox="0 0 16 14"><path d="M8 13L2 7a3.5 3.5 0 0 1 6-4 3.5 3.5 0 0 1 6 4z" fill="none" stroke="#fff" stroke-width="1.4"/></svg></div></div>
    </div>
    <div class="row1"><span class="name">COFFEE BEAN</span><span class="price"><s>$100</s>$ 85</span></div>
    <div class="row2"><span>Chocolate, Caramel. 1 kg</span><span class="stars">★★★★☆</span></div>
  </div>
  <div class="abs product" style="left:784px">
    <div class="photo" role="img" aria-label="Two paper coffee bags on a wooden counter"></div>
    <div class="row1"><span class="name">COFFEE BEAN</span><span class="price"><s>$100</s>$ 85</span></div>
    <div class="row2"><span>Jammy fruitiness. 1 kg</span><span class="stars">★★★★☆</span></div>
  </div>
</section>

<section>
  <div class="abs deliver-img" role="img" aria-label="Steel coffee canister with scattered beans on a table"></div>
  <div class="abs deliver-box">
    <h2>DELIVERED TO YOU</h2>
    <p>To provide you with an unparalleled home roasting experience, the Hearthline subscription service and mobile app allows you to choose your beans from all over the world, with our suggestions for different roasts. That way, you can explore and enjoy a range of flavors each time you roast.</p>
  </div>
  <div class="abs deliver-badge">Kornhaus</div>
</section>

<section class="abs newsletter" role="img" aria-label="Coffee beans border on a light textured background">
  <h2>NEWSLETTER SIGN UP</h2>
  <div class="field">enter your email address</div>
  <div class="subscribe">SUBSCRIBE</div>
</section>

<footer>
  <div class="abs footer">
    <div class="badge">Kornhaus</div>
    <div class="contact" style="top:128px"><svg width="10" height="14" viewBox="0 0 10 14"><path d="M5 13S1 8 1 5a4 4 0 0 1 8 0c0 3-4 8-4 8z" fill="#6a3414"/><circle cx="5" cy="5" r="1.5" fill="#fff"/></svg><span>Business Address:<br>218 Millbrook Lane, Unit 7<br>Building 4<br>Fairhaven, OR 97120</span></div>
    <div class="contact" style="top:196px"><svg width="12" height="9" viewBox="0 0 12 9"><rect width="12" height="9" fill="#6a3414"/><path d="M0 0l6 5 6-5" fill="none" stroke="#fff"/></svg><span>info@kornhaus-roast.com</span></div>
    <div class="col" style="left:447px"><h5>MORE INFORMATION</h5><ul><li>About</li><li>Bestsellers</li><li>Blog and News</li><li>Charging Technology</li><li>Contact Us</li><li>Distributors</li><li>Press/Media Resources</li><li>Partner Influencer Program</li></ul></div>
    <div class="col" style="left:687px"><h5>SUPPORT</h5><ul><li>Wholesale/Bulk Orders</li><li>Privacy Policy</li><li>Helpdesk</li><li>Shipping &amp; Tracking</li><li>Contact Us</li></ul></div>
    <div class="col" style="left:901px"><h5>STAY CONNECTED</h5><div class="social"><i></i><i></i><i></i><i></i></div></div>
  </div>
  <div class="abs cup" role="img" aria-label="Cup of coffee beside scattered beans"></div>
  <div class="abs copy">© 2019 Kornhaus. All Rights Reserved</div>
</footer>
</body>
</html>
```